Holiday Graphic for Cover of Catalog

We're looking for a design that represents the Holiday season to use on the cover of this year's holiday catalog. You can take a look at 2011's catalog at this link: http://paglerow.com/tindlecrest/docs/holiday_gift_guide. Your design should not be a replication, but it can be inspired by the cover of 2011's Catalog.

Please create a design that is WINTER-specific, not necessarily Christmas, Hanukkah, or any other holiday-specific design. Something simple, modern, contemporary is preferable. The design should have a specific color scheme & that scheme should be easily detectable by a viewer.

Options for The final size of the front-cover:
a. 8.5"width x 5.405"height
b. 8.5"width x 10.81"height
c. 10.81"height x 8.5"width
d. square 8.5" x 8.5"

Please note: I do not have the time or budget to have these printed with foil stamping, so please avoid any metallic finishes.  

Thanks!
Rosa

Requirements
Must have
• Our logo, attached file.
• Title: "2013 Holiday Gift Giving Guide"

```html
<!DOCTYPE html>
<html lang="en">
<head>
<meta charset="utf-8">
<title>Holiday Gift Giving Guide 2013</title>
<link rel="stylesheet" href="https://fonts.googleapis.com/css2?family=Great+Vibes&family=Raleway:wght@200;300;600&display=swap">
<style>
  :root {
    --page: #ffffff;
    --maroon: #710021;
    --flake: rgba(196, 110, 132, 0.55);
    --script: #ffffff;
    --ribbon: #c8c8c8;
    --ribbon-stitch: #555555;
    --guide-ink: #2e2e2e;
    --year: #ffffff;
    --badge: #ffffff;
    --brand-ink: #1a1a1a;
  }
  * { margin: 0; padding: 0; box-sizing: border-box; }
  html, body {
    width: 1064px; height: 1200px; overflow: hidden;
    background: var(--page);
  }
  .cover {
    position: absolute; left: 51px; top: 115px;
    width: 960px; height: 958px;
    background: var(--maroon);
    overflow: hidden;
  }
  .snowflake {
    position: absolute; border-radius: 50%;
    background: radial-gradient(circle, var(--flake) 0%, rgba(196,110,132,0.35) 45%, rgba(196,110,132,0) 72%);
  }
  .snowflake--top-left { left: -40px; top: -110px; width: 460px; height: 460px; }
  .snowflake--top-right { left: 680px; top: 0; width: 340px; height: 340px; }
  .snowflake--right { left: 720px; top: 570px; width: 300px; height: 300px; }
  .snowflake--bottom-left { left: 20px; top: 600px; width: 400px; height: 400px; }
  .snowflake--bottom { left: 610px; top: 720px; width: 190px; height: 190px; }

  .title-script {
    position: absolute; left: 0; width: 100%;
    text-align: center; color: var(--script);
    font-family: "Great Vibes", cursive; font-weight: 400;
    line-height: 1;
  }
  .title-script--holiday { top: 140px; font-size: 118px; }
  .title-script--gift { top: 255px; font-size: 170px; letter-spacing: -2px; }

  .ribbon {
    position: absolute; left: 55px; top: 464px;
    width: 845px; height: 142px;
  }
  .ribbon__word {
    position: absolute; left: 0; top: 0; width: 100%; height: 100%;
    display: flex; align-items: center; justify-content: center;
    font-family: "Raleway", sans-serif; font-weight: 300;
    font-size: 112px; letter-spacing: 4px; color: var(--guide-ink);
  }
  .title-script--over { z-index: 2; }

  .year {
    position: absolute; left: 0; top: 640px; width: 100%;
    display: flex; align-items: center; justify-content: center; gap: 26px;
    font-family: "Raleway", sans-serif; font-weight: 200;
    font-size: 76px; letter-spacing: 6px; color: var(--year);
  }
  .year__tree { width: 40px; height: 56px; }

  .brand-badge {
    position: absolute; left: 377px; top: 780px;
    width: 196px; height: 142px;
    background: var(--badge); border-radius: 8px;
    display: flex; align-items: center; justify-content: center;
  }
  .brand-badge__name {
    font-family: "Raleway", sans-serif; font-weight: 600;
    font-size: 27px; color: var(--brand-ink); letter-spacing: 0.5px;
  }
</style>
</head>
<body>
  <main class="cover">
    <div class="snowflake snowflake--top-left" role="img" aria-label="Large faint snowflake"></div>
    <div class="snowflake snowflake--top-right" role="img" aria-label="Faint snowflake"></div>
    <div class="snowflake snowflake--right" role="img" aria-label="Faint snowflake"></div>
    <div class="snowflake snowflake--bottom-left" role="img" aria-label="Large faint snowflake"></div>
    <div class="snowflake snowflake--bottom" role="img" aria-label="Small faint snowflake"></div>

    <div class="ribbon">
      <svg width="845" height="142" viewBox="0 0 845 142">
        <polygon points="0,0 845,0 808,71 845,142 0,142 37,71" fill="var(--ribbon)"/>
        <polyline points="10,8 835,8 800,71 835,134 10,134 45,71 10,8" fill="none"
                  stroke="var(--ribbon-stitch)" stroke-width="3" stroke-dasharray="2 5"/>
      </svg>
      <div class="ribbon__word">GUIDE</div>
    </div>

    <h1>
      <span class="title-script title-script--holiday title-script--over">Holiday</span>
      <span class="title-script title-script--gift title-script--over">Gift Giving</span>
    </h1>

    <div class="year">
      <svg class="year__tree" viewBox="0 0 40 56" aria-hidden="true">
        <polygon points="20,0 32,16 8,16" fill="#fff"/>
        <polygon points="20,10 36,30 4,30" fill="#fff"/>
        <polygon points="20,22 40,46 0,46" fill="#fff"/>
        <rect x="17" y="46" width="6" height="10" fill="#fff"/>
      </svg>
      <span>2013</span>
      <svg class="year__tree" viewBox="0 0 40 56" aria-hidden="true">
        <polygon points="20,0 32,16 8,16" fill="#fff"/>
        <polygon points="20,10 36,30 4,30" fill="#fff"/>
        <polygon points="20,22 40,46 0,46" fill="#fff"/>
        <rect x="17" y="46" width="6" height="10" fill="#fff"/>
      </svg>
    </div>

    <div class="brand-badge">
      <span class="brand-badge__name">TINDLECREST</span>
    </div>
  </main>
</body>
</html>
```